Webdesign for Dutch IT consultancy company

Make a Wordpress webdesign for a Dutch consultancy company

Briefing Brivola IT

Website for finding and connecting IT-professionals. Corebusiness is to find IT-professionals and to help them to follow their ambitions. We offer training, personal coaching and education trajects.

U can take www.Tavemko.nl as an example for the website.

Home page

U can take www.Tavemko.nl as an example.

There should be jobs on the home page. A block for short info about us and about what whe do and a trigger to contact us quickly.

Jobs Page

On this page should be the jobs that we offer for the professionals. There should be a search function on this page so u can easily find the job that you are looking for.

A call to action can be on this page too.

Also a little block with text for some information.

For professionals page

Block with information on top. Call to action. info about who we work for/with.

For Clients

Info about three different solutions

- Sourcing solutions
- Consultancy solutions
- Custom based traineeships

Request a qoute option

Traineeships page

Info about two different traineeships

- Linux traineeships
- Microsoft traineeships

Call to action/ subscribe for traineeships

About us page

We are BrivolaT IT

Our mission: Creating cooperations between young professionals and businesses who wanna work on a great future.

Our core values

Last news

Target Market(s)

Young professionals and businesses who need IT services

Industry/Entity Type

It Company

Coding

Coded - Design and coding required

Number of Pages Required

5+ page

Font styles to use
Other font styles liked:
• Calibri

Colors
ffffff
add136
6b449b

Requirements
Must have
• Home page, Jobs Page, Professionals page, Clients page, Traineeships page, About us Page
• Green and/or Purple layout. Job search option, subscribe option
Nice to have
• modern design

```html
<!DOCTYPE html>
<html lang="en">
<head>
<meta charset="utf-8">
<title>Brivola IT</title>
<link href="https://fonts.googleapis.com/css2?family=Open+Sans:wght@400;600;700&display=swap" rel="stylesheet">
<style>
:root{
  --purple:#6b449b;
  --purple-deep:#4b1f62;
  --purple-btn:#553a74;
  --green:#add136;
  --green-soft:#a4cb38;
  --ink:#333;
  --muted:#666;
  --line:#e6e6e6;
  --footer:#2e2a31;
  --footer-bar:#1f1c21;
  --white:#fff;
}
*{box-sizing:border-box;margin:0;padding:0}
html,body{width:1200px;height:2631px;overflow:hidden}
body{font-family:"Open Sans",Arial,sans-serif;color:var(--ink);background:var(--white);position:relative}
.abs{position:absolute}

/* header */
.site-header{position:absolute;left:0;top:0;width:1200px;height:91px;background:var(--white);z-index:2}
.brand{position:absolute;left:172px;top:36px;font-size:26px;font-weight:700;color:var(--purple);letter-spacing:.5px}
.main-nav{position:absolute;left:415px;top:44px;display:flex;gap:27px;font-size:13px;color:#444}
.main-nav .active{color:var(--purple)}
.main-nav .has-sub::after{content:"⌄";font-size:11px;margin-left:3px}

/* hero */
.hero{position:absolute;left:0;top:91px;width:1200px;height:439px;background:linear-gradient(180deg,#6a4a6e 0%,#7d6a6a 45%,#5f6f3c 80%,#4f6135 100%)}
.hero-title{position:absolute;left:0;top:196px;width:1200px;text-align:center;color:var(--white);font-size:21px;font-weight:700;letter-spacing:1px;line-height:40px;text-transform:uppercase}
.hero-actions{position:absolute;top:302px;left:0;width:1200px;display:flex;justify-content:center;gap:8px}
.btn{display:inline-block;font-size:12px;text-transform:uppercase;padding:7px 15px;font-weight:600;letter-spacing:.3px}
.btn-light{background:#eee;color:#333}
.btn-purple{background:var(--purple);color:var(--white)}

/* jobs */
.section-title{font-size:18px;font-weight:700;color:#222}
.jobs-title{left:174px;top:573px}
.jobs-rule{left:162px;top:618px;width:573px;height:2px;background:var(--purple);opacity:.5}
.job{position:absolute;left:162px;width:573px;border-bottom:1px solid var(--line)}
.job.tint-yellow{background:#fdfdf0}
.job.tint-green{background:#f4f9ef;border-bottom:2px solid #c7df8f}
.job-logo{position:absolute;left:18px;top:34px;width:48px;height:48px;border:1px solid #ddd;background:#fff;font-size:8px;font-weight:700;color:var(--purple);display:flex;align-items:center;justify-content:center;text-align:center;line-height:10px;padding:2px}
.job-name{position:absolute;left:88px;top:28px;font-size:15px;color:#333}
.job-meta{position:absolute;left:88px;top:62px;font-size:11.5px;color:#555;display:flex;gap:14px;white-space:nowrap}
.job-meta svg{vertical-align:-2px;margin-right:5px}
.view-more{left:340px;top:1158px;width:229px;height:38px;background:var(--purple-btn);color:#fff;font-size:12px;font-weight:700;display:flex;align-items:center;justify-content:center;gap:7px}

.spot-title{left:760px;top:573px}
.spot-arrows{left:998px;top:572px;font-size:18px;color:#555;letter-spacing:6px}
.spotlight{left:759px;top:619px;width:269px;height:326px;border:1px solid var(--line);background:#fff}
.spotlight h3{font-size:14px;font-weight:400;color:#444;line-height:21px;position:absolute;left:16px;top:28px;width:200px}
.spot-row{position:absolute;left:16px;font-size:11px;color:#555;width:230px;display:flex;gap:10px;line-height:15px}
.spotlight p{position:absolute;left:22px;top:182px;width:228px;font-size:10.5px;line-height:16px;color:#555}
.apply{position:absolute;left:46px;top:276px;width:176px;height:34px;background:var(--purple-btn);color:#fff;font-size:11px;font-weight:700;display:flex;align-items:center;justify-content:center}
.upload{left:759px;top:963px;width:269px;height:168px;background:#f3f3f5}
.upload h3{text-align:center;font-size:15px;font-weight:600;color:#333;margin-top:20px}
.upload p{text-align:center;font-size:10px;color:#777;line-height:15px;padding:8px 26px 0}
.upload .btn-upload{position:absolute;left:59px;top:116px;width:152px;height:35px;background:var(--purple-btn);color:#fff;font-size:11px;font-weight:700;display:flex;align-items:center;justify-content:center}

/* about & quote */
.about{left:0;top:1237px;width:595px;height:437px;background:linear-gradient(135deg,#5e8a2e 0%,#7fa640 55%,#6e9a35 100%)}
.about h2{position:absolute;left:186px;top:50px;color:#fff;font-size:19px;font-weight:700}
.rule-white{position:absolute;height:2px;width:40px;background:#fff}
.about p{position:absolute;left:186px;width:360px;color:#fff;font-size:12px;line-height:20px}
.quote{left:595px;top:1237px;width:605px;height:437px;background:var(--green-soft)}
.quote h2{position:absolute;left:34px;top:52px;color:#fff;font-size:19px;font-weight:600}
.quote .sub{position:absolute;left:34px;top:87px;color:#fff;font-size:11.5px}
.field{position:absolute;background:#fff;font-size:11px;color:#777;padding:9px 6px}
.submit{position:absolute;left:36px;top:345px;width:100px;height:34px;background:#fff;color:#222;font-size:11px;font-weight:700;display:flex;align-items:center;justify-content:center}

/* services */
.services-title{left:0;top:1727px;width:1200px;text-align:center}
.services-rule{left:580px;top:1766px;width:40px;height:2px;background:var(--purple)}
.services-lead{left:0;top:1771px;width:1200px;text-align:center;font-size:12.5px;color:#555}
.people{left:0;top:1780px;width:314px;height:329px;background:linear-gradient(180deg,#e9e9ee 0%,#3a3f4a 70%,#2b2f38 100%)}
.service{position:absolute;top:1846px;height:158px;background:#fff;box-shadow:0 1px 6px rgba(0,0,0,.14);text-align:center}
.service .icon{width:58px;height:58px;border-radius:50%;border:2px solid #d9c8ec;margin:-23px auto 0;background:#fff;display:flex;align-items:center;justify-content:center}
.service h3{font-size:14px;font-weight:600;color:#333;margin-top:14px;letter-spacing:.4px}
.service p{font-size:10.5px;color:#666;line-height:16px;margin:8px 18px 0}

/* cta */
.cta{left:0;top:2109px;width:1200px;height:219px;background:linear-gradient(90deg,#5a2a6e 0%,#4e2166 100%)}
.cta h2{position:absolute;left:0;top:65px;width:1200px;text-align:center;color:#fff;font-size:23px;font-weight:400;letter-spacing:.6px}
.cta .btn-contact{position:absolute;left:544px;top:142px;width:112px;height:33px;background:#fff;color:#222;font-size:11px;font-weight:700;display:flex;align-items:center;justify-content:center}

/* footer */
.site-footer{left:0;top:2328px;width:1200px;height:265px;background:var(--footer);color:#ddd}
.foot-title{position:absolute;top:34px;font-size:15px;font-weight:700;color:#fff}
.foot-rule{position:absolute;top:62px;width:60px;height:2px;background:#888}
.contact-row{position:absolute;left:182px;display:flex;gap:18px;font-size:11.5px;color:#eee;line-height:17px;width:240px}
.links{position:absolute;top:106px;font-size:11.5px;line-height:20px;color:#eee}
.socials{position:absolute;left:202px;top:215px;display:flex;gap:9px}
.socials span{width:9px;height:9px;border-radius:50%;background:#eee}
.foot-quote{position:absolute;left:479px;top:203px;width:155px;height:34px;background:var(--purple);color:#fff;font-size:13px;font-weight:600;display:flex;align-items:center;justify-content:center}
.map{position:absolute;left:766px;top:88px;width:250px;height:168px;background:linear-gradient(135deg,#e9e6d8 0%,#cfdde6 50%,#e8e2cc 100%)}
.to-top{position:absolute;left:1094px;top:201px;width:26px;height:26px;background:var(--purple);transform:rotate(45deg)}
.bottom-bar{left:0;top:2593px;width:1200px;height:38px;background:var(--footer-bar);color:#ccc;font-size:10.5px;padding:12px 172px}
</style>
</head>
<body>

<header class="site-header">
  <div class="brand">Brivola IT</div>
  <nav class="main-nav">
    <span class="active">Home</span>
    <span class="has-sub">Jobs</span>
    <span class="has-sub">For Professionals</span>
    <span class="has-sub">For Clients</span>
    <span class="has-sub">Traineeships</span>
    <span class="has-sub">About Us</span>
    <span>Contact Us</span>
  </nav>
</header>

<section class="hero" role="img" aria-label="Photo of two young professionals sitting on grass working on a laptop">
  <h1 class="hero-title">Creating cooperations between professionals and businesses<br>who wanna work on a great future</h1>
  <div class="hero-actions">
    <span class="btn btn-light">IT Vacancies</span>
    <span class="btn btn-purple">Request a Quote</span>
  </div>
</section>

<h2 class="abs section-title jobs-title">Recent It Jobs</h2>
<div class="abs jobs-rule"></div>

<article class="job tint-yellow" style="top:627px;height:120px">
  <div class="job-logo">Linkwave Info</div>
  <div class="job-name">Network Engineer</div>
  <div class="job-meta">
    <span><svg width="11" height="10"><rect x="0" y="2" width="11" height="8" fill="#777"/><rect x="3" y="0" width="5" height="3" fill="none" stroke="#777"/></svg>Linkwave Info</span>
    <span><svg width="8" height="11"><path d="M4 0a4 4 0 0 1 4 4c0 3-4 7-4 7S0 7 0 4a4 4 0 0 1 4-4z" fill="#777"/></svg>115,Cillum dolore eu fugiat nulla pariatur</span>
    <span><svg width="12" height="9"><rect x=".5" y=".5" width="11" height="8" fill="none" stroke="#777"/><circle cx="6" cy="4.5" r="2" fill="#777"/></svg>$40000 - $50000</span>
  </div>
</article>
<article class="job tint-green" style="top:749px;height:125px">
  <div class="job-logo">Datora</div>
  <div class="job-name">Software Developer</div>
  <div class="job-meta">
    <span><svg width="11" height="10"><rect x="0" y="2" width="11" height="8" fill="#777"/><rect x="3" y="0" width="5" height="3" fill="none" stroke="#777"/></svg>Datora</span>
    <span><svg width="8" height="11"><path d="M4 0a4 4 0 0 1 4 4c0 3-4 7-4 7S0 7 0 4a4 4 0 0 1 4-4z" fill="#777"/></svg>115,Aut reiciendis voluptatibus maiores</span>
    <span><svg width="12" height="9"><rect x=".5" y=".5" width="11" height="8" fill="none" stroke="#777"/><circle cx="6" cy="4.5" r="2" fill="#777"/></svg>$30000 - $60000</span>
  </div>
</article>
<article class="job" style="top:876px;height:127px">
  <div class="job-logo" style="top:38px">Kestrel Aero</div>
  <div class="job-name">Project Manager</div>
  <div class="job-meta">
    <span><svg width="11" height="10"><rect x="0" y="2" width="11" height="8" fill="#777"/><rect x="3" y="0" width="5" height="3" fill="none" stroke="#777"/></svg>Kestrel Aerospace</span>
    <span><svg width="8" height="11"><path d="M4 0a4 4 0 0 1 4 4c0 3-4 7-4 7S0 7 0 4a4 4 0 0 1 4-4z" fill="#777"/></svg>115,Cumque nihil impedit quo minus</span>
    <span><svg width="12" height="9"><rect x=".5" y=".5" width="11" height="8" fill="none" stroke="#777"/><circle cx="6" cy="4.5" r="2" fill="#777"/></svg>$35000 - $50000</span>
  </div>
</article>
<article class="job" style="top:1004px;height:126px">
  <div class="job-logo" style="top:38px">Pellow</div>
  <div class="job-name">Computer and Information Expert</div>
  <div class="job-meta">
    <span><svg width="11" height="10"><rect x="0" y="2" width="11" height="8" fill="#777"/><rect x="3" y="0" width="5" height="3" fill="none" stroke="#777"/></svg>Pellow Packaging</span>
    <span><svg width="8" height="11"><path d="M4 0a4 4 0 0 1 4 4c0 3-4 7-4 7S0 7 0 4a4 4 0 0 1 4-4z" fill="#777"/></svg>115,Reiciendis voluptatibus maiores</span>
    <span><svg width="12" height="9"><rect x=".5" y=".5" width="11" height="8" fill="none" stroke="#777"/><circle cx="6" cy="4.5" r="2" fill="#777"/></svg>$40000 - $50000</span>
  </div>
</article>
<div class="abs view-more"><svg width="12" height="12"><circle cx="6" cy="6" r="6" fill="#fff"/><path d="M3 6h6M6 3v6" stroke="#553a74" stroke-width="2"/></svg>VIEW MORE JOBS</div>

<h2 class="abs section-title spot-title">Job Spotlight</h2>
<div class="abs spot-arrows">‹ ›</div>
<aside class="abs spotlight">
  <h3>Senior Onsite Support Engineer</h3>
  <div class="spot-row" style="top:88px"><svg width="11" height="10"><rect x="0" y="2" width="11" height="8" fill="#777"/></svg>Norvik Industrial</div>
  <div class="spot-row" style="top:113px"><svg width="8" height="11" style="flex:none"><path d="M4 0a4 4 0 0 1 4 4c0 3-4 7-4 7S0 7 0 4a4 4 0 0 1 4-4z" fill="#777"/></svg>15A/1,Cum soluta nobis est eligendi optio cumque</div>
  <div class="spot-row" style="top:151px"><svg width="12" height="9"><rect x=".5" y=".5" width="11" height="8" fill="none" stroke="#777"/></svg>$30000 - $35000</div>
  <p>Nostrum exercitationem ullam corporis suscipit laboriosam, nisi ut aliquid ex ea commodi in ea voluptate velit esse quam nihil molestiae</p>
  <div class="apply">APPLY FOR THIS JOB</div>
</aside>
<aside class="abs upload">
  <h3>Upload Your Resume</h3>
  <p>Nemo enim ipsam voluptatem quia voluptas sit aspernatur aut odit aut fugit, sed quia consequuntur ratione voluptatem sequi</p>
  <div class="btn-upload">UPLOAD RESUME</div>
</aside>

<section class="abs about" role="img" aria-label="Green tinted photo of business people reviewing documents">
  <h2>About Brivola IT</h2>
  <div class="rule-white" style="left:186px;top:84px"></div>
  <p style="top:128px">Corebusiness is to find IT-professionals and to help them to follow their ambitions.</p>
  <p style="top:175px">Our mission is to: Creating cooperations between young professionals and businesses who wanna work on a great future.</p>
</section>
<section class="abs quote">
  <h2>Request a Quote</h2>
  <div class="sub">Numquam eius modi tempora incidunt</div>
  <div class="rule-white" style="left:34px;top:114px;width:28px"></div>
  <div class="field" style="left:36px;top:146px;width:180px;height:29px">First Name *</div>
  <div class="field" style="left:243px;top:146px;width:180px;height:29px">Last Name *</div>
  <div class="field" style="left:36px;top:190px;width:180px;height:29px">Email...</div>
  <div class="field" style="left:243px;top:190px;width:180px;height:29px">Phone No...</div>
  <div class="field" style="left:36px;top:236px;width:387px;height:84px">Message...</div>
  <div class="submit">SUBMIT</div>
</section>

<h2 class="abs section-title services-title">Our Services</h2>
<div class="abs services-rule"></div>
<p class="abs services-lead" style="top:1774px">Reprehenderit qui in ea voluptate velit esse quam nihil molestiae</p>
<div class="abs people" role="img" aria-label="Photo of a smiling businessman and businesswoman in suits"></div>

<div class="service" style="left:348px;width:200px">
  <div class="icon"><svg width="30" height="30" fill="none" stroke="#6b449b" stroke-width="1.5"><rect x="4" y="8" width="16" height="18"/><path d="M8 14h8M8 18h8M8 22h5M18 4l8 8"/></svg></div>
  <h3>CONSULTANCY</h3>
  <p>Neque porro quisquam est qui dolorem ipsum quia dolor</p>
</div>
<div class="service" style="left:569px;width:206px">
  <div class="icon"><svg width="30" height="30" fill="none" stroke="#6b449b" stroke-width="1.5"><rect x="4" y="5" width="22" height="15"/><path d="M15 20v6M10 27l5-7 5 7M8 15l5-5 4 3 5-5"/></svg></div>
  <h3>TRAINING</h3>
  <p>Quis nostrud exercitation ullamco laboris nisi ut ea commodo</p>
</div>
<div class="service" style="left:787px;width:207px">
  <div class="icon"><svg width="30" height="30" fill="none" stroke="#6b449b" stroke-width="1.5"><circle cx="15" cy="15" r="11"/><path d="M15 4v22M15 15l7-6"/></svg></div>
  <h3>SECONDMENT</h3>
  <p>Ipsam voluptatem quia voluptas sit aspernatur aut odit aut</p>
</div>

<section class="abs cta" role="img" aria-label="Purple tinted photo of hands typing on a laptop keyboard">
  <h2>Finding and Connecting IT-professionals</h2>
  <div class="btn-contact">CONTACT US</div>
</section>

<footer class="abs site-footer">
  <h3 class="foot-title" style="left:182px">CONTACT US</h3>
  <div class="foot-rule" style="left:182px"></div>
  <div class="contact-row" style="top:93px"><svg width="9" height="12" style="flex:none;margin-top:2px"><path d="M4.5 0a4.5 4.5 0 0 1 4.5 4.5C9 8 4.5 12 4.5 12S0 8 0 4.5A4.5 4.5 0 0 1 4.5 0z" fill="#eee"/></svg>12/1, reiciendis voluptatibus maiores alias consequatur</div>
  <div class="contact-row" style="top:139px"><svg width="10" height="11" style="flex:none;margin-top:3px"><path d="M1 1l3 0 1 3-2 1a7 7 0 0 0 3 3l1-2 3 1v3C5 10 1 6 1 1z" fill="#eee"/></svg>0850 200 300</div>
  <div class="contact-row" style="top:168px"><svg width="11" height="9" style="flex:none;margin-top:4px"><rect width="11" height="9" fill="#eee"/><path d="M0 0l5.5 5L11 0" stroke="#2e2a31" fill="none"/></svg>info@brivolait.com</div>
  <div class="socials"><span></span><span></span><span></span><span></span></div>

  <h3 class="foot-title" style="left:467px">USEFUL LINKS</h3>
  <div class="foot-rule" style="left:467px"></div>
  <div class="links" style="left:467px">About Us<br>Traineeships<br>For Professionals<br>Contact Us</div>
  <div class="links" style="left:584px">For Clients<br>Custom based traineeships<br>News<br>Privacy Policy</div>
  <div class="foot-quote">REQUEST A QUOTE</div>

  <h3 class="foot-title" style="left:760px">LOCATE US</h3>
  <div class="foot-rule" style="left:760px"></div>
  <div class="map" role="img" aria-label="Street map showing the office location near Amsterdam"></div>
  <div class="to-top"></div>
</footer>
<div class="abs bottom-bar">©Copyright information here</div>

</body>
</html>
```